A simple Chatterbook Ad (not Chatterbook Page) for weight loss surgery

It’s a simple ad in terms of the text.

The text should say:
Curious about weight loss surgery?
This 30 second quiz will tell you which procedure will suit you best

I'm open to variations in the text if it is thought to enhance the ad.

Targeted towards obese individuals who have been unable to lose weight with diet and exercise. My industry is weight loss surgery – webpage www.marcusbellweather.com.au. Clicking the ad leads to a quiz on my webpage relating to weight loss surgery. Most frequent users of this service are females (75%) between ages of 35 and 55 years.

Successful weight loss surgery can enable individuals who have been unable to lose weight to lose a substantial amount of the excess weight they are carrying to be healthier and happier.

```html
<!DOCTYPE html>
<html lang="en">
<head>
<meta charset="utf-8">
<title>Weight Loss Surgery Quiz Ad</title>
<link rel="stylesheet" href="https://fonts.googleapis.com/css2?family=Anton&family=Playfair+Display:ital,wght@1,800;1,900&display=swap">
<style>
  :root {
    --teal: #3fcdbd;
    --teal-light: #6fe0d2;
    --teal-deep: #22a89c;
    --navy: #10223a;
    --white: #ffffff;
    --photo-light: #dfe6cc;
    --photo-mid: #a8c391;
    --photo-teal: #3fb7b0;
  }
  html, body {
    margin: 0;
    padding: 0;
    width: 1200px;
    height: 1200px;
    overflow: hidden;
    background: var(--white);
  }
  .ad {
    position: relative;
    width: 1200px;
    height: 1200px;
    overflow: hidden;
  }
  .ad-shapes {
    position: absolute;
    inset: 0;
  }
  .headline {
    position: absolute;
    left: 96px;
    top: 176px;
    margin: 0;
    font-family: "Anton", "Impact", sans-serif;
    font-weight: 400;
    text-transform: uppercase;
    letter-spacing: 0.5px;
  }
  .headline-lead {
    display: block;
    color: var(--navy);
    font-size: 82px;
    line-height: 96px;
  }
  .headline-main {
    display: block;
    color: var(--white);
    font-size: 108px;
    line-height: 106px;
  }
  .subline {
    position: absolute;
    left: 98px;
    top: 522px;
    width: 480px;
    margin: 0;
    font-family: "Playfair Display", "Georgia", serif;
    font-style: italic;
    font-weight: 900;
    font-size: 54px;
    line-height: 60px;
    letter-spacing: -0.5px;
    color: var(--navy);
  }
  .subline-accent {
    color: var(--white);
  }
  .cta {
    position: absolute;
    left: 99px;
    top: 846px;
    width: 258px;
    height: 92px;
    background: var(--navy);
    color: var(--teal);
    font-family: "Anton", "Impact", sans-serif;
    font-size: 42px;
    line-height: 92px;
    text-align: center;
    letter-spacing: 0.5px;
    text-transform: uppercase;
  }
</style>
</head>
<body>
<main class="ad">
  <svg class="ad-shapes" width="1200" height="1200" viewBox="0 0 1200 1200">
    <defs>
      <linearGradient id="photoGradient" x1="0" y1="0" x2="1" y2="0.4">
        <stop offset="0" stop-color="var(--photo-light)"/>
        <stop offset="0.5" stop-color="var(--photo-mid)"/>
        <stop offset="1" stop-color="var(--photo-teal)"/>
      </linearGradient>
      <linearGradient id="tealBand" x1="0" y1="0" x2="1" y2="1">
        <stop offset="0" stop-color="var(--teal)" stop-opacity="0.9"/>
        <stop offset="1" stop-color="var(--teal-deep)" stop-opacity="0.9"/>
      </linearGradient>
    </defs>

    <rect class="photo-area" x="0" y="0" width="1200" height="1200" fill="url(#photoGradient)" role="img"
          aria-label="Photo: woman in teal workout clothes and headphones with a towel around her neck, resting after exercise in a green park"/>

    <polygon class="teal-band" points="0,0 490,0 1200,710 1200,1200 760,1200 0,410" fill="url(#tealBand)"/>
    <polygon class="teal-band-highlight" points="0,0 420,0 0,290" fill="var(--teal-light)" opacity="0.3"/>

    <line class="accent-line" x1="660" y1="40" x2="692" y2="76" stroke="var(--teal-deep)" stroke-width="3"/>
    <line class="accent-line" x1="250" y1="810" x2="498" y2="1068" stroke="var(--teal-deep)" stroke-width="3"/>
  </svg>

  <h1 class="headline">
    <span class="headline-lead">Curious about</span>
    <span class="headline-main">Weight loss</span>
    <span class="headline-main">surgery?</span>
  </h1>

  <p class="subline">This <span class="subline-accent">30 second</span> quiz will tell you which procedure will suit you best!</p>

  <div class="cta">Take now</div>
</main>
</body>
</html>
```